Flyer Design Project

We are a coaching organisation that is about to launch classes catering to local and international university students in Australia. We would like a flyer that is fresh, captivating and ultimately pushes people to our website.
To understand the artistic approach to our business, visit our website: www.brightlanetutors.com.au
Updates
Hi designers, we have changed the criteria slightly to give you more creative license... Feel free to ask any questions, all the best.
Target Market(s)
International University Students aged between 18-25
Industry/Entity Type
University
Requirements
Must have
- Size: 1 sided A5 flyer
Must have logo on page
Introductory offer of 20% off all courses
Bright Lane Tutors exists to help university students with real life skill development such as public speaking. We aim to equip students with skills that are not taught in the university environment to enable them to maximise their results.
To find out more visit: www.brightlanetutors.com.au
CONTACT DETAILS: Leave space for 10 digit phone number
Nice to have
- Bold, eye catching design
Fresh, fun and professional look
Good use of typography
Should not have
- Do not use colours outside or that do not compliment our colour palette. You can view our three main colours (blue, pink, yellow) on our website.
www.brightlanetutors.com.au/courses/publicspeaking

```html
<!DOCTYPE html>
<html lang="en">
<head>
<meta charset="utf-8">
<title>Bright Lane Tutors – Flyer</title>
<link rel="stylesheet" href="https://fonts.googleapis.com/css2?family=Arimo:ital,wght@0,400;0,700;1,700&family=Questrial&family=Ubuntu:ital,wght@1,400&family=Noto+Sans+SC:wght@400;700&display=swap">
<style>
  :root{
    --blue:#1f8fd6;
    --blue-light:#2aa9e6;
    --navy:#1e4fa0;
    --pink:#e32b4d;
    --pink-light:#f0485f;
    --yellow:#f7e81c;
    --yellow-light:#fff56b;
    --ink:#2b5aa8;
    --charcoal:#3a3a3c;
    --paper:#ffffff;
    --paper-shade:#ececec;
  }
  *{margin:0;padding:0;box-sizing:border-box}
  html,body{width:856px;height:1200px;overflow:hidden;background:#fff}
  .flyer{position:relative;width:856px;height:1200px;overflow:hidden;
    background:radial-gradient(ellipse at 45% 45%,var(--paper) 55%,var(--paper-shade) 100%);
    font-family:"Arimo",Arial,sans-serif}
  .art{position:absolute;left:0;top:0}
  .brand{position:absolute;left:58px;top:62px;display:flex;align-items:center;gap:24px}
  .brand-dot{width:74px;height:74px;border-radius:50%;background:var(--blue);flex:none}
  .brand-name{font-family:"Questrial",sans-serif;font-weight:400;color:var(--navy);font-size:56px;line-height:56px;letter-spacing:-0.5px}
  .offer{position:absolute;left:0;top:0;width:856px;height:340px;color:#fff;font-weight:700;font-style:italic}
  .offer span{position:absolute;display:block;text-align:center;white-space:nowrap}
  .offer-lead{left:530px;width:224px;top:130px;font-size:29px;line-height:34px}
  .offer-pct{left:552px;width:150px;top:198px;font-size:66px;line-height:70px;color:var(--yellow);font-style:normal}
  .offer-off{left:698px;width:56px;top:196px;font-size:33px;line-height:38px}
  .offer-tail{left:540px;width:210px;top:262px;font-size:29px;line-height:32px}
  .benefits{position:absolute;left:0;top:0;width:856px;list-style:none}
  .pill{position:absolute;height:58px;border-radius:29px;display:flex;align-items:center;justify-content:center;
    font-size:27px;font-weight:700;white-space:nowrap;box-shadow:0 3px 5px rgba(0,0,0,.18)}
  .pill .zh{font-family:"Noto Sans SC",sans-serif;font-size:32px;font-weight:400;margin-left:8px}
  .pill .zh b{font-weight:700}
  .pill-blue{background:linear-gradient(var(--blue-light),var(--blue));color:#fff}
  .pill-pink{background:linear-gradient(var(--pink-light),var(--pink));color:#fff}
  .pill-yellow{background:linear-gradient(var(--yellow-light),var(--yellow));color:#111}
  .about{position:absolute;left:116px;top:808px;width:616px;font-family:"Questrial",sans-serif;
    color:var(--ink);font-size:22.5px;line-height:29.5px}
  .about span{display:block;text-align:justify;text-align-last:justify}
  .about span:last-child{text-align-last:left}
  .contact{position:absolute;left:30px;top:1117px;color:#fff;font-size:19.5px;line-height:33px}
  .contact li{list-style:none;display:flex;align-items:center;gap:12px}
  .web{position:absolute;right:28px;top:1149px;color:#fff;font-size:23px;display:flex;align-items:center;gap:8px}
</style>
</head>
<body>
<main class="flyer">
  <svg class="art" width="856" height="1200" viewBox="0 0 856 1200" aria-hidden="true">
    <path class="corner-swoosh" d="M483 0 H856 V56 C760 40 620 20 483 0 Z" fill="#d9d9db"/>
    <path class="swoosh-red" d="M0 176 C140 240 300 282 440 283 L440 288 C300 292 130 258 0 192 Z" fill="var(--pink)"/>
    <path class="swoosh-blue" d="M39 181 C180 240 330 270 480 270 L480 277 C330 282 170 252 39 186 Z" fill="var(--navy)"/>
    <path class="swoosh-yellow" d="M266 242 C340 252 420 256 490 254 L490 262 C420 264 340 258 266 246 Z" fill="var(--yellow)"/>
    <path d="M790 228 C815 222 836 216 856 208 V228 C836 236 815 242 790 248 Z" fill="var(--yellow)"/>
    <path d="M790 248 C815 242 836 236 856 228 V248 C836 256 815 262 790 268 Z" fill="#2a2d6e"/>
    <g class="starburst" transform="translate(642 210) scale(1.03 0.73) rotate(-4)">
      <polygon fill="var(--pink)" stroke="#fff" stroke-width="7" stroke-linejoin="round" vector-effect="non-scaling-stroke"
        points="180,0 137,27 166,69 116,78 127,127 78,116 69,166 27,137 0,180 -27,137 -69,166 -78,116 -127,127 -116,78 -166,69 -137,27 -180,0 -137,-27 -166,-69 -116,-78 -127,-127 -78,-116 -69,-166 -27,-137 0,-180 27,-137 69,-166 78,-116 127,-127 116,-78 166,-69 137,-27"/>
    </g>
    <path class="band-charcoal" d="M0 952 C250 1032 560 1032 856 986 V1070 C560 1112 250 1110 0 1035 Z" fill="var(--charcoal)"/>
    <path class="band-blue" d="M0 1035 C250 1110 560 1112 856 1068 V1200 H0 Z" fill="var(--navy)"/>
    <path id="tagline-path" d="M92 1042 C280 1095 480 1100 710 1062" fill="none"/>
    <text font-family="Ubuntu, sans-serif" font-style="italic" font-size="46" fill="var(--yellow)">
      <textPath href="#tagline-path">BE YOUR BEST. GET IN LANE.</textPath>
    </text>
    <circle class="seal" cx="746" cy="1000" r="46" fill="var(--blue)"/>
  </svg>

  <header class="brand">
    <span class="brand-dot"></span>
    <h1 class="brand-name">Bright Lane<br>Tutors</h1>
  </header>

  <p class="offer">
    <span class="offer-lead">Introductory<br>offer of</span>
    <span class="offer-pct">20%</span>
    <span class="offer-off">off</span>
    <span class="offer-tail">all courses</span>
  </p>

  <ul class="benefits">
    <li class="pill pill-blue" style="left:172px;top:385px;width:512px">Chosen Subjects /<span class="zh">选中的科目</span></li>
    <li class="pill pill-pink" style="left:143px;top:466px;width:569px">Received Timetable /<span class="zh"><b>收到的</b>时间表</span></li>
    <li class="pill pill-yellow" style="left:28px;top:546px;width:800px">Confident in Public Speaking /<span class="zh"><b>在公开</b>场合自信演讲</span></li>
    <li class="pill pill-pink" style="left:143px;top:626px;width:569px">Fridge full of Volt Fizz /<span class="zh">满冰箱的能量饮料</span></li>
    <li class="pill pill-blue" style="left:99px;top:706px;width:658px">Prepared to be my very best /<span class="zh"><b>做最好的自己</b></span></li>
  </ul>

  <p class="about">
    <span>Bright Lane Tutors exists to help university students</span>
    <span>with real life skill development such as public</span>
    <span>speaking. We aim to equip students with skills that</span>
    <span>are not taught in the university environment to</span>
    <span>enable them to maximise their results.</span>
  </p>

  <ul class="contact">
    <li>
      <svg width="22" height="22" viewBox="0 0 22 22" aria-hidden="true"><circle cx="11" cy="11" r="10" fill="none" stroke="#fff" stroke-width="1.6"/><path d="M7 6 l2 -1 2 3 -1.5 1.2 c.6 1.6 1.6 2.8 3 3.4 l1.3 -1.4 3 2 -1 2.1 c-4.5 .2 -9 -4.5 -8.8 -9.3 z" fill="#fff"/></svg>
      Call: 555-010-2468
    </li>
    <li>
      <svg width="22" height="16" viewBox="0 0 22 16" aria-hidden="true"><rect x="1" y="1" width="20" height="14" fill="none" stroke="#fff" stroke-width="1.6"/><path d="M1 1 L11 9 L21 1" fill="none" stroke="#fff" stroke-width="1.6"/></svg>
      inquiries@brightlanetutors.com.au
    </li>
  </ul>
  <p class="web">www.brightlanetutors.com.au
    <svg width="20" height="20" viewBox="0 0 20 20" aria-hidden="true"><g fill="none" stroke="#fff" stroke-width="1.4"><circle cx="10" cy="10" r="8.5"/><ellipse cx="10" cy="10" rx="4" ry="8.5"/><path d="M1.5 10 H18.5 M3 5.5 H17 M3 14.5 H17"/></g></svg>
  </p>
</main>
</body>
</html>
```